Brisk Motion Studio Chinese New Year Special

We want to attract new people to our gym

I will be looking for a graphic that we can use for posting on our PX and making flyers. We are a coin operated fitness center, much like a laundromat without the washers and dryers, but treadmills instead.

-I want to make it clear that we are not a regular gym that we don't have contracts(its pay as you go) and we don't have sales people to hassle anyone.

-The main theme is Chinese New Years (so Chinese New Year colors and designs appropriate).

-If we use people exercising I would like them to look Chinese and be on a piece of cardio equipment, but not weights, we do not have weights.

-Our colors are yellow and black.

-we'd like to draw likes to our PX page

-call to action is buy 40 tokens and get 10 free. Must send shipping address to our PX message service. Then we will send tokens COD. PX:BRISKMOTIONSTUDIO

-In the end you will need to change all of the text to Chinese. I will give you the text to replace what you create.
Updates

Target Market(s)

Target to women interested in fitness, weight loss, wellness, etc. between the ages of 18 - 50. We accept men too, but I would like the over all appeal to women. Safe, gentle, warm, inviting, etc... since we are 24 hours, I want this image.

Industry/Entity Type

Fitness

Font styles to use
Sans Serif

Colors
fbee3f
262626
ec1f27

Requirements
Must have
• Like us in PX
• Yellow and black
• Chinese New Year Theme
• Buy 40 tokens get 10 free + special coin purse (I'll add a picture). Send PX message to order.
• Club locations - I'll send a map.
• Phone number
• Our logo and name Brisk Motion Studio
• Tag line "We are not a normal gym"
Nice to have
• Your personal touch, give our message a unifying theme and make the design warm, comfortable, and safe.
Should not have
• Some of the photos are just for example. I would like this project to have a different look from previous designs, but provide all of the correct information.

```html
<!DOCTYPE html>
<html lang="en">
<head>
<meta charset="utf-8">
<title>Brisk Motion Studio Chinese New Year Special</title>
<link rel="stylesheet" href="https://fonts.googleapis.com/css2?family=Anton&family=Lato:wght@400;700&family=Lobster&display=swap">
<style>
  :root {
    --page: #e4e4e4;
    --red-deep: #8e0d0d;
    --red: #c3161a;
    --yellow: #fbee3f;
    --gold: #e8c21a;
    --ink: #262626;
    --ink-brown: #2a0f0c;
    --white: #ffffff;
    --orange: #ec7424;
    --map: #d8d2bf;
  }
  * { margin: 0; padding: 0; box-sizing: border-box; }
  html, body { width: 1200px; height: 1200px; overflow: hidden; background: var(--page); }
  .flyer {
    position: absolute; left: 153px; top: 22px;
    width: 1015px; height: 1314px;
    transform: scale(0.88); transform-origin: 0 0;
    overflow: hidden;
    background: radial-gradient(ellipse at 30% 40%, var(--red) 0%, var(--red-deep) 70%, #6d0909 100%);
    font-family: 'Lato', sans-serif; color: var(--white);
  }
  .lantern-art {
    position: absolute; right: 0; top: 0; width: 520px; height: 760px;
    background: radial-gradient(ellipse at 75% 35%, #e02a1c 0%, #c8241a 40%, rgba(180,20,20,0) 75%),
                radial-gradient(circle at 85% 60%, rgba(240,190,40,0.55) 0%, rgba(240,190,40,0) 35%);
  }
  .sparkle-art {
    position: absolute; left: 0; top: 860px; width: 1015px; height: 220px;
    background: linear-gradient(180deg, rgba(150,10,10,0) 0%, rgba(210,40,40,0.45) 100%);
  }
  .band {
    position: absolute; left: 0; top: 1057px; width: 1015px; height: 257px;
    background: linear-gradient(180deg, #f4e22a 0%, var(--yellow) 60%, #f1d91f 100%);
  }
  .shapes { position: absolute; inset: 0; }
  .brand {
    position: absolute; left: 36px; top: 120px; width: 250px;
    display: flex; align-items: center; gap: 10px;
    font-weight: 700; font-size: 27px; color: var(--ink); line-height: 1.1;
  }
  .brand-dot { width: 34px; height: 34px; border-radius: 50%; background: var(--gold); flex: none; }
  .open {
    position: absolute; left: 346px; top: 142px;
    display: flex; align-items: center; gap: 14px;
    font-size: 29px; letter-spacing: 0.5px;
  }
  .open-badge { display: flex; }
  .open-badge span {
    width: 40px; height: 40px; border: 4px solid var(--white); border-radius: 50%;
    display: flex; align-items: center; justify-content: center;
    font-size: 17px; font-weight: 700; margin-right: -6px;
  }
  .rule { position: absolute; height: 2px; background: var(--white); }
  .tagline { font-family: 'Lobster', cursive; font-size: 40px; line-height: 1; }
  .tagline span { position: absolute; white-space: nowrap; }
  .perks { position: absolute; left: 61px; top: 352px; list-style: none; }
  .perks li {
    display: flex; align-items: center; gap: 28px; height: 97px;
    font-family: 'Anton', sans-serif; font-size: 58px; letter-spacing: 1px;
  }
  .intro {
    position: absolute; left: 59px; top: 658px; width: 462px;
    font-size: 22px; line-height: 30px;
  }
  .phone {
    position: absolute; left: 59px; top: 871px;
    display: flex; align-items: center; gap: 22px;
    font-family: 'Anton', sans-serif; font-size: 62px; line-height: 1; letter-spacing: 1px;
  }
  .social {
    position: absolute; left: 62px; top: 955px;
    display: flex; align-items: center; gap: 20px;
    font-weight: 700; font-size: 27px; color: var(--gold);
  }
  .social-mark {
    width: 60px; height: 60px; border-radius: 50%; background: var(--white);
    color: var(--red-deep); display: flex; align-items: center; justify-content: center; font-size: 24px;
  }
  .offer-head { position: absolute; left: 609px; top: 644px; display: flex; align-items: center; gap: 18px; color: var(--ink-brown); font-family: 'Anton', sans-serif; }
  .offer-num { font-size: 118px; line-height: 1; }
  .offer-word { font-size: 46px; line-height: 52px; }
  .offer-rule { position: absolute; left: 681px; top: 773px; width: 113px; height: 3px; background: var(--ink-brown); }
  .offer-sub { position: absolute; left: 587px; top: 788px; width: 300px; text-align: center; color: var(--red); font-size: 27px; line-height: 34px; }
</style>
</head>
<body>
<main class="flyer">
  <div class="lantern-art" role="img" aria-label="Red Chinese New Year lantern with golden tassels"></div>
  <div class="sparkle-art" role="img" aria-label="Sparkling red festive glitter"></div>
  <div class="band" role="img" aria-label="Yellow-toned gym interior with cardio machines"></div>

  <svg class="shapes" width="1015" height="1314" viewBox="0 0 1015 1314">
    <defs>
      <linearGradient id="runner-tone" x1="0" y1="0" x2="1" y2="1">
        <stop offset="0" stop-color="#3f6b3a"/>
        <stop offset="0.6" stop-color="#7c9a6a"/>
        <stop offset="1" stop-color="#9aa59a"/>
      </linearGradient>
    </defs>
    <path class="logo-panel" d="M0 0 H285 L362 82 Q372 97 362 110 L150 322 Q136 336 122 324 L0 216 Z" fill="var(--white)"/>
    <path d="M911 674 L1015 572 L1015 776 Z" fill="var(--orange)"/>
    <path d="M776 959 L975 760 Q988 744 1005 744 L1015 744 L1015 1166 Z" fill="url(#runner-tone)" role="img" aria-label="Woman jogging outdoors in a park"/>
    <rect x="590" y="605" width="294" height="294" rx="34" transform="rotate(45 737 752)" fill="var(--yellow)"/>
    <g fill="var(--map)" role="img" aria-label="Street maps to the four studio locations">
      <rect x="97" y="1074" width="166" height="166" rx="22" transform="rotate(45 180 1157)"/>
      <rect x="315" y="1074" width="166" height="166" rx="22" transform="rotate(45 398 1157)"/>
      <rect x="531" y="1074" width="166" height="166" rx="22" transform="rotate(45 614 1157)"/>
      <rect x="745" y="1074" width="166" height="166" rx="22" transform="rotate(45 828 1157)"/>
    </g>
  </svg>

  <div class="brand"><span class="brand-dot"></span>Brisk Motion Studio</div>

  <div class="open">WE ARE OPEN <span class="open-badge"><span>24</span><span>7</span></span></div>
  <div class="rule" style="left:300px;top:200px;width:421px"></div>
  <p class="tagline">
    <span style="left:276px;top:210px">We make exericse simple,</span>
    <span style="left:222px;top:247px">come in and give us a try!</span>
  </p>
  <div class="rule" style="left:179px;top:297px;width:444px"></div>

  <ul class="perks">
    <li><svg width="54" height="54" viewBox="0 0 54 54"><rect x="3" y="10" width="40" height="40" fill="none" stroke="var(--gold)" stroke-width="5"/><path d="M13 28 L23 38 L50 6" fill="none" stroke="var(--gold)" stroke-width="6"/></svg>NO SALES PEOPLE</li>
    <li><svg width="54" height="54" viewBox="0 0 54 54"><rect x="3" y="10" width="40" height="40" fill="none" stroke="var(--gold)" stroke-width="5"/><path d="M13 28 L23 38 L50 6" fill="none" stroke="var(--gold)" stroke-width="6"/></svg>NO CONTRACTS</li>
    <li><svg width="54" height="54" viewBox="0 0 54 54"><rect x="3" y="10" width="40" height="40" fill="none" stroke="var(--gold)" stroke-width="5"/><path d="M13 28 L23 38 L50 6" fill="none" stroke="var(--gold)" stroke-width="6"/></svg>NO HASSLE</li>
  </ul>

  <p class="intro">We are not a normal gym. At Brisk Motion Studio you pay for each twenty minute segment and you do not have to sign a contract or commit to time in the future. You can simply pay as you go. We have one of the most affordable price plans in Taiwan.</p>

  <div class="phone">
    <svg width="30" height="52" viewBox="0 0 30 52"><rect x="2" y="2" width="26" height="48" rx="4" fill="none" stroke="var(--gold)" stroke-width="4"/><line x1="10" y1="8" x2="20" y2="8" stroke="var(--gold)" stroke-width="3"/></svg>
    0955246810
  </div>

  <div class="social">Like us in <span class="social-mark">PX</span></div>

  <section class="offer">
    <div class="offer-head"><span class="offer-num">40</span><span class="offer-word">BUY<br>TOKENS</span></div>
    <div class="offer-rule"></div>
    <p class="offer-sub">GET 10 FREE +<br>SPECIAL COIN<br>PURSE</p>
  </section>
</main>
</body>
</html>
```